law firm business cards

I need a business card using my existing logo. Two sided is best because there is a lot of information that needs to go on the card. Use the same general color scheme as logo, but I need one set with the blue background of my website (www.kestonlegalgroup.com), and one set with white background (to see which one I like best).

Information that must be on there:
Darren P. Holloway
Board Certified Civil Trial Specialist
738 Brindlewood Ave., Suite 2300
Raleigh, NC 27699

T 919-555-0142
F 919-555-0187

www.kestonlegalgroup.com
darren@kestonlegalgroup.com

Personal Injury | Criminal Law (to separate the two, pls use a bullet point or pipeline symbol "|"

If there is a way to work in the QRVC logo (maybe at the bottom somewhere), put it in, but don't let it detract from the main logo too much.

Also, if there is a way to work it in, put in somewhere: Former Insurance Company Attorney | Former Criminal Prosecutor (to separate the two, pls use a bullet point or pipeline symbol "|"

```html
<!DOCTYPE html>
<html lang="en">
<head>
<meta charset="utf-8">
<title>Keston Law – Business Cards</title>
<link rel="stylesheet" href="https://fonts.googleapis.com/css2?family=Cinzel:wght@400;600&family=Lato:wght@300;400;700&display=swap">
<style>
  :root {
    --backdrop: #d9dadc;
    --navy: #1b3a6b;
    --navy-deep: #163260;
    --blue: #3f82c4;
    --blue-light: #6aa6da;
    --sky: #cfe0f2;
    --red: #e0202e;
    --white: #ffffff;
    --serif: "Cinzel", "Times New Roman", serif;
    --sans: "Lato", "Helvetica Neue", Arial, sans-serif;
  }
  * { box-sizing: border-box; margin: 0; padding: 0; }
  html, body { width: 1200px; height: 1000px; overflow: hidden; }
  body { background: var(--backdrop); position: relative; }

  .card {
    position: absolute;
    width: 700px;
    height: 400px;
    left: 250px;
    border-radius: 42px;
    overflow: hidden;
    box-shadow: 0 8px 24px rgba(0,0,0,0.18);
  }
  .card-front { top: 70px; }
  .card-back { top: 530px; background: var(--white); }
  .card-art { position: absolute; inset: 0; width: 100%; height: 100%; }

  .firm-name {
    position: absolute;
    font-family: var(--serif);
    font-weight: 400;
    line-height: 1;
    letter-spacing: 1px;
    white-space: nowrap;
  }
  .card-front .firm-name {
    left: 82px; top: 74px;
    font-size: 54px;
    color: var(--white);
  }
  .card-back .firm-name {
    right: 46px; top: 50px;
    font-size: 38px;
    color: var(--navy);
  }
  .firm-mark {
    position: absolute;
    border-radius: 50%;
  }
  .card-front .firm-mark { left: 40px; top: 88px; width: 28px; height: 28px; background: var(--white); }
  .card-back .firm-mark { right: 328px; top: 56px; width: 24px; height: 24px; background: var(--navy); }

  .attorney {
    position: absolute;
    left: 268px; top: 178px;
    color: var(--white);
    font-family: var(--sans);
  }
  .attorney-name { font-size: 28px; font-weight: 700; letter-spacing: 0.5px; line-height: 1.2; }
  .attorney-title { font-size: 18px; font-weight: 300; margin-top: 2px; }

  .former-roles {
    position: absolute;
    right: 70px; top: 278px;
    text-align: right;
    font-family: var(--serif);
    font-size: 19px;
    line-height: 1.2;
    letter-spacing: 2.5px;
    color: var(--sky);
  }

  .practice-areas {
    position: absolute;
    left: 44px; top: 22px;
    font-family: var(--serif);
    font-size: 13px;
    letter-spacing: 5px;
    color: var(--blue-light);
  }

  .contact {
    position: absolute;
    right: 46px; top: 140px;
    text-align: right;
    color: var(--white);
    font-family: var(--sans);
    font-size: 17px;
    font-weight: 400;
    line-height: 1.35;
  }
  .contact .web { font-size: 22px; font-weight: 700; margin-top: 4px; letter-spacing: 0.5px; }

  .certification-seal {
    position: absolute;
    left: 150px; top: 296px;
    width: 58px; height: 58px;
    border-radius: 50%;
    border: 2px solid #8a93a3;
    background: #f4f6f9;
  }
</style>
</head>
<body>

  <section class="card card-front" aria-label="Business card front">
    <svg class="card-art" viewBox="0 0 700 400" preserveAspectRatio="none" aria-hidden="true">
      <defs>
        <linearGradient id="frontFill" x1="0" y1="0" x2="1" y2="1">
          <stop offset="0" stop-color="#163260"/>
          <stop offset="0.45" stop-color="#2b5fa0"/>
          <stop offset="1" stop-color="#4d95d1"/>
        </linearGradient>
        <linearGradient id="frontSweep" x1="0" y1="0" x2="1" y2="0">
          <stop offset="0" stop-color="#ffffff" stop-opacity="0.3"/>
          <stop offset="1" stop-color="#ffffff" stop-opacity="0"/>
        </linearGradient>
      </defs>
      <rect width="700" height="400" fill="url(#frontFill)"/>
      <path d="M0 270 C 200 190, 450 150, 700 140 L700 0 L0 0 Z" fill="#1b3a6b" opacity="0.5"/>
      <path d="M0 350 C 180 250, 420 200, 700 190" stroke="url(#frontSweep)" stroke-width="36" fill="none"/>
      <path d="M0 395 C 220 290, 460 240, 700 230" stroke="#ffffff" stroke-opacity="0.1" stroke-width="16" fill="none"/>
      <path d="M50 208 C 230 160, 440 138, 650 132" stroke="var(--red)" stroke-width="4" fill="none"/>
    </svg>
    <span class="firm-mark" aria-hidden="true"></span>
    <div class="firm-name">KESTON LAW</div>
    <div class="attorney">
      <div class="attorney-name">Darren P. Holloway</div>
      <div class="attorney-title">Board Certified Civil Trial Specialist</div>
    </div>
    <div class="former-roles">
      <div>FORMER INSURANCE COMPANY ATTORNEY</div>
      <div>FORMER CRIMINAL PROSECUTOR</div>
    </div>
  </section>

  <section class="card card-back" aria-label="Business card back">
    <svg class="card-art" viewBox="0 0 700 400" preserveAspectRatio="none" aria-hidden="true">
      <defs>
        <linearGradient id="backFill" x1="0" y1="0" x2="1" y2="1">
          <stop offset="0" stop-color="#5f9fd8"/>
          <stop offset="1" stop-color="#2f6fb5"/>
        </linearGradient>
      </defs>
      <rect width="700" height="400" fill="#ffffff"/>
      <path d="M0 400 L0 300 C 90 185, 240 105, 700 84 L700 400 Z" fill="#e3edf8"/>
      <path d="M0 400 L0 330 C 100 190, 250 110, 700 96 L700 400 Z" fill="url(#backFill)"/>
      <path d="M0 380 C 200 260, 450 200, 700 180" stroke="#ffffff" stroke-opacity="0.18" stroke-width="14" fill="none"/>
      <path d="M310 120 C 430 108, 560 100, 690 94" stroke="var(--red)" stroke-width="3.5" fill="none"/>
    </svg>
    <div class="practice-areas">PERSONAL INJURY | CRIMINAL LAW</div>
    <span class="firm-mark" aria-hidden="true"></span>
    <div class="firm-name">KESTON LAW</div>
    <div class="contact">
      <div>738 Brindlewood Ave., Suite 2300</div>
      <div>Raleigh, NC 27699</div>
      <div>T 919-555-0142&nbsp;&nbsp;F 919-555-0187</div>
      <div>darren@kestonlegalgroup.com</div>
      <div class="web">www.kestonlegalgroup.com</div>
    </div>
    <div class="certification-seal" role="img" aria-label="Board certification seal"></div>
  </section>

</body>
</html>
```